DL Gift Voucher

I need a DL sized gift voucher designed based on and incorporating my attached logo and the fonts therein. It should include the following elements:
Gift Certificate
To:_____________ (this should be a long line)
From:___________ (this should also be a long line)
Amount:________ (small line - enough for 4 digit number with dollar sign)
Authorised signature: ____ (small line)
Expiry Date: ________ (small line)
Ph. 0417 583 926
www.larkwoodimaging.biz
Updates
Thank you to all the designers who have put the effort in to submit designs but I have pretty much chose one now. I'm sorry if you were eliminated - there were many great designs, it's a shame I can only choose one!

```html
<!DOCTYPE html>
<html lang="en">
<head>
<meta charset="utf-8">
<title>Larkwood Imaging – DL Gift Certificate</title>
<link href="https://fonts.googleapis.com/css2?family=Pinyon+Script&family=Federo&family=Lora&display=swap" rel="stylesheet">
<style>
  :root {
    --taupe: #8c8278;
    --paper: #ffffff;
    --ink: #111111;
    --edge: #2a2a2a;
    --rule: #f4f1ee;
  }
  * { margin: 0; padding: 0; box-sizing: border-box; }
  html, body { width: 1200px; height: 1000px; overflow: hidden; background: var(--paper); }
  .sheet { position: relative; width: 1200px; height: 1000px; }

  .side-label {
    position: absolute; left: 61px;
    font: 44px/1 Arial, Helvetica, sans-serif; color: var(--ink);
  }
  .side-label--front { top: 448px; }
  .side-label--back { top: 925px; }

  .voucher {
    position: absolute; left: 61px; width: 1093px; height: 364px;
    border: 1px solid var(--edge); background: var(--paper);
  }
  .voucher--front { top: 67px; }
  .voucher--back { top: 543px; }

  .brand-panel {
    position: absolute; left: 0; top: 0; width: 272px; height: 100%;
  }
  .brand-name {
    position: absolute; left: 0; width: 100%; text-align: center;
    font-family: "Pinyon Script", cursive; color: var(--taupe); font-weight: 400;
  }
  .brand-panel .brand-name { top: 70px; font-size: 46px; line-height: 58px; }

  .contact-phone {
    position: absolute; top: 278px; width: 100%; text-align: center;
    font: 31px/1 "Federo", sans-serif; color: var(--taupe); letter-spacing: 1px;
  }
  .contact-web {
    position: absolute; top: 331px; width: 100%; text-align: center;
    font: 14px/1 "Lora", serif; color: var(--taupe);
  }

  .detail-panel {
    position: absolute; left: 272px; top: 0; right: 0; height: 100%;
    background: var(--taupe); color: var(--paper);
    font-family: "Pinyon Script", cursive;
  }
  .detail-title {
    position: absolute; left: 0; right: 0; top: 14px; text-align: center;
    font-size: 50px; line-height: 1;
  }
  .field { position: absolute; display: flex; align-items: flex-end; }
  .field-label { line-height: 1; white-space: nowrap; }
  .field-line { border-bottom: 1.5px solid var(--rule); margin-left: 6px; height: 1px; margin-bottom: 4px; }

  .field--to { left: 34px; top: 128px; font-size: 40px; }
  .field--to .field-line { width: 335px; }
  .field--from { left: 34px; top: 200px; font-size: 40px; }
  .field--from .field-line { width: 287px; }
  .field--amount { left: 520px; top: 146px; font-size: 22px; }
  .field--amount .field-line { width: 113px; }
  .field--expiry { left: 478px; top: 218px; font-size: 22px; }
  .field--expiry .field-line { width: 113px; }
  .field--signature { left: 334px; top: 301px; font-size: 22px; }
  .field--signature .field-line { width: 190px; margin-left: 2px; }

  .voucher--back .brand-name { top: 120px; font-size: 76px; line-height: 84px; }
</style>
</head>
<body>
<main class="sheet">
  <section class="voucher voucher--front" aria-label="Gift certificate front">
    <div class="brand-panel">
      <p class="brand-name">Larkwood<br>Imaging</p>
      <p class="contact-phone">0417 583 926</p>
      <p class="contact-web">www.larkwoodimaging.biz</p>
    </div>
    <div class="detail-panel">
      <h1 class="detail-title">Gift Certificate</h1>
      <div class="field field--to"><span class="field-label">To:</span><span class="field-line"></span></div>
      <div class="field field--amount"><span class="field-label">Amount:</span><span class="field-line"></span></div>
      <div class="field field--from"><span class="field-label">From:</span><span class="field-line"></span></div>
      <div class="field field--expiry"><span class="field-label">Expiry Date:</span><span class="field-line"></span></div>
      <div class="field field--signature"><span class="field-label">Authorised Signature:</span><span class="field-line"></span></div>
    </div>
  </section>
  <p class="side-label side-label--front">Front</p>

  <section class="voucher voucher--back" aria-label="Gift certificate back">
    <p class="brand-name">Larkwood<br>Imaging</p>
  </section>
  <p class="side-label side-label--back">Back</p>
</main>
</body>
</html>
```